Packaging Design Job - Baby Diaper Rash Cream and Wipes Packaging Concepts Needed

Hello, Our baby brand “Pellora” is launching 2 new products – a Diaper Rash Cream and Diaper Wipes – and would like some creative design concepts for our product packaging.Pellora is a pharmaceutical brand that specializes in baby products. We are a mid – premium priced brand with a focus on targeting mothers between the ages of 18 – 35 years. Our products are positioned for mass market with other competitive brands such as Malvotex, Bramolux, Harvonel, and Quilbrat, to give you a better understanding of the category. What we are looking for in our packaging is an ethical, pharmaceutical look that will appeal to mothers as a product that is safe and effective for their baby. The packaging should be clean, fresh, and consumer friendly, while still maintaining that this is a clinical product. The design concepts are a box design for the Diaper Rash Cream and a plastic packaging design for the Diaper Wipes. Attached you will find the Pellora logo and examples of Diaper Rash Cream box packaging and Diaper Wipes plastic packaging from competitors (to give you an idea of what shape of packaging we like). Please feel free to contact me should you have any questions.Thank you for your time and effort,Roxa

Target Market(s)

We are a mid – premium priced brand with a focus on targeting mothers between the ages of 18 – 35 years.

Industry/Entity Type

Baby Care

Requirements
Must have
• Packaging design concepts for a box design for the Diaper Rash Cream and a plastic packaging design for the Diaper Wipes.
Nice to have
• Diaper Rash Cream box: 8 cm width, 8 cm length, 8 cm depth
• Diaper Wipes package: 23 cm width, 10.5 cm length, 4.5 cm depth

```html
<!DOCTYPE html>
<html lang="en">
<head>
<meta charset="utf-8">
<title>Pellora Baby Wipes – Pack Front</title>
<link href="https://fonts.googleapis.com/css2?family=Barlow:wght@400&display=swap" rel="stylesheet">
<style>
  :root {
    --backdrop: #e2e2e2;
    --pack-white: #ffffff;
    --wave-blue: #d8edf4;
    --wave-blue-light: #e8f5fa;
    --brand-blue: #1d6fa3;
    --lid-line: #d9d9d9;
    --art-blue: #cfe5f0;
  }
  * { margin: 0; padding: 0; box-sizing: border-box; }
  html, body {
    width: 1200px;
    height: 701px;
    overflow: hidden;
    background: var(--backdrop);
    font-family: "Barlow", sans-serif;
  }
  .pack-front {
    position: absolute;
    left: 190px;
    top: 125px;
    width: 850px;
    height: 400px;
    background: var(--pack-white);
    overflow: hidden;
  }
  .wave-band {
    position: absolute;
    inset: 0;
    width: 850px;
    height: 400px;
  }
  .baby-art {
    position: absolute;
    left: 122px;
    top: 49px;
    width: 134px;
    height: 220px;
    border-radius: 67px;
    background: linear-gradient(180deg, var(--art-blue), var(--wave-blue-light));
  }
  .dispenser-lid {
    position: absolute;
    left: 292px;
    top: 119px;
    width: 300px;
    height: 164px;
  }
  .product-name {
    position: absolute;
    left: 572px;
    top: 76px;
    font-size: 35px;
    line-height: 1;
    font-weight: 400;
    letter-spacing: 1.5px;
    white-space: nowrap;
    color: var(--brand-blue);
  }
  .brand-mark {
    position: absolute;
    left: 552px;
    top: 276px;
    display: flex;
    align-items: center;
    gap: 10px;
  }
  .brand-dot {
    width: 18px;
    height: 18px;
    border-radius: 50%;
    background: var(--brand-blue);
  }
  .brand-name {
    font-size: 46px;
    font-weight: 400;
    letter-spacing: 2px;
    line-height: 1;
    white-space: nowrap;
    color: var(--brand-blue);
  }
</style>
</head>
<body>
  <main class="pack-front">
    <svg class="wave-band" viewBox="0 0 850 400" aria-hidden="true">
      <path fill="var(--wave-blue)"
        d="M0,307 C200,302 420,262 520,125 S590,10 615,0 L850,0 L850,129
           C650,160 520,220 430,270 S180,366 0,363 Z"/>
    </svg>

    <div class="baby-art" role="img" aria-label="Line illustration of a swaddled baby"></div>

    <svg class="dispenser-lid" viewBox="0 0 300 164" aria-hidden="true">
      <path fill="none" stroke="var(--lid-line)" stroke-width="2"
        d="M12,1 H270 Q284,1 284,15 V58 Q296,64 296,82 Q296,100 284,106 V149 Q284,163 270,163 H12 Q1,163 1,149 V15 Q1,1 12,1 Z"/>
    </svg>

    <h1 class="product-name">Baby wipes</h1>

    <div class="brand-mark">
      <span class="brand-dot"></span>
      <span class="brand-name">PELLORA</span>
    </div>
  </main>
</body>
</html>
```